Flyer Design Project for Sports Medicine Services

I am a sports medicine doctor specialising in the diagnosis and management of sport and exercise injuries for all ages and levels of activity - from elite to weekend jogger. I work under the Business name Peak Motion Athletic Care and do have a company logo. I am wanting a flier that I can send to family doctors, physiotherapists and sports clubs explaining who I am what I can offer and why they should send me patients.
- I have a Masters in Sports Medicine (MSportsMed), Diplomas in Obstetrics/Gynaecology (DRANZCOG) and also Paediatrics (DCH) and certificate in advanced clinical hypnosis
-accurate diagnosis and management plan with their regular physio to return the player / athlete to the field / court /gym as soon as safely possible
-hypnosis for sports performance eg anxiety control, confidence and mental rehearsal for individuals and teams
- because there are many possible therapists and therapy options, as a sports doctor I can work out who they need to see a physiotherapist, surgeon, massage therapist chiropractor or podiatrist to return them to activity or whether cortisone, PRP or autologous blood injections are needed
-can provide one point of contact for coaches and clubs for rehabilitation and return to sport advice.
- work with Clara Hutchings ex Australian Athlete, a Performance Strategist (NRC listed resource person) and registered Psychologist for best mental preparation for individuals teams and coach development
- can organise rapid access to MRI, ultrasound and specialist appointments if needed
-I work at 3 practices KineCore 418 Tolley Rd Kestrel Vale 84619032 Monday Wednesday Friday; Harrow Lane Sports Clinic, 153 Denholm Rd, Adelaide 81764290 Tuesday Riverbend Falcons Sports Medicine Clinic, Norvale Park 8291 6475 Thursday.
-facebook site peakmotionathleticcare
Updates
Hi All, just to clarify.. My name is Paul Denton and I am the sports doctor. My wife is Clara Hutchings and she is the psychologist. The flier should mainly be advertising my sports medicine services and a byline ( or at least not the first line in the title) about the Performance Strategy and Coach development.
Target Market(s)
family doctors (GPs), Sporting Clubs, Physiotherapists
Industry/Entity Type
Massage
Look and feel

```html
<!DOCTYPE html>
<html lang="en">
<head>
<meta charset="utf-8">
<title>Dr. Paul Denton – Peak Motion Athletic Care</title>
<link rel="stylesheet" href="https://fonts.googleapis.com/css2?family=Arimo:ital,wght@0,400;0,700;1,400;1,700&display=swap">
<style>
  :root {
    --frame-blue: #7fd0f0;
    --accent-blue: #3bb7e8;
    --heading-blue: #41b9ea;
    --ink: #111111;
    --paper: #ffffff;
    --panel-white: rgba(255, 255, 255, 0.88);
    --wall: #b9ab96;
    --wall-dark: #6f6454;
    --lightbox: #2c3f7a;
  }
  * { margin: 0; padding: 0; box-sizing: border-box; }
  html, body { width: 1200px; height: 768px; overflow: hidden; background: var(--paper); }
  body { font-family: "Arimo", Arial, sans-serif; color: var(--ink); }

  .flyer { position: relative; width: 1200px; height: 768px; overflow: hidden; }

  .hero-photo {
    position: absolute; inset: 0;
    background:
      linear-gradient(90deg, transparent 0 520px, rgba(44,63,122,0.85) 540px, rgba(70,95,160,0.8) 900px, rgba(44,63,122,0.85) 1130px, transparent 1150px),
      linear-gradient(180deg, var(--wall) 0%, #a89a85 55%, var(--wall-dark) 100%);
  }
  .hero-photo::after {
    content: ""; position: absolute; left: 530px; top: 70px; width: 610px; height: 450px;
    background: radial-gradient(ellipse at 50% 50%, rgba(159,180,230,0.35), transparent 70%);
  }

  .side-panel { position: absolute; inset: 0; width: 1200px; height: 768px; }

  .frame {
    position: absolute; inset: 0;
    border: 11px solid var(--frame-blue);
    border-top-width: 9px;
    pointer-events: none;
  }

  .brand {
    position: absolute; left: 30px; top: 62px; width: 170px;
    text-align: center;
  }
  .brand-dot {
    display: block; width: 40px; height: 40px; border-radius: 50%;
    background: var(--accent-blue); margin: 0 auto 12px;
  }
  .brand-name {
    font-size: 17px; font-weight: 700; line-height: 1.15; color: var(--accent-blue);
  }
  .brand-address {
    position: absolute; left: 12px; top: 181px; width: 210px;
    font-size: 12.5px; line-height: 1.35; text-align: center;
  }

  .practice-list {
    position: absolute; left: 29px; top: 434px;
    font-size: 16.3px; line-height: 20.9px; list-style: none;
  }
  .practice-list li + li { margin-top: 20.9px; }

  .website {
    position: absolute; left: 302px; top: 739px; font-size: 12.5px;
  }

  .doctor-name {
    position: absolute; left: 250px; top: 44px;
    font-size: 42px; font-weight: 700; font-style: italic; letter-spacing: 0.5px;
    color: var(--paper);
    text-shadow: 3px 3px 4px rgba(0,0,0,0.45);
  }

  .info-panel {
    position: absolute; left: 680px; top: 96px; width: 458px; height: 638px;
    background: var(--panel-white);
    padding: 34px 8px 0 27px;
    font-size: 16.6px; line-height: 20.8px;
  }
  .info-panel ul { list-style: none; }
  .lead {
    font-size: 18.6px; font-weight: 700; line-height: 23px; margin-bottom: 19px;
  }
  .section-title {
    color: var(--heading-blue); font-style: italic; font-weight: 400;
    font-size: 18.6px; line-height: 21px;
  }
  .section-title.offers { margin-top: 19px; }
</style>
</head>
<body>
<main class="flyer">
  <div class="hero-photo" role="img" aria-label="Photograph of the smiling doctor with a stethoscope in front of an illuminated x-ray lightbox"></div>

  <svg class="side-panel" viewBox="0 0 1200 768" aria-hidden="true">
    <path d="M0,0 L200,0 C235,300 360,610 600,768 L0,768 Z" fill="#ffffff"/>
    <path d="M200,0 C235,300 360,610 600,768" fill="none" stroke="#7fd0f0" stroke-width="16"/>
  </svg>

  <div class="frame"></div>

  <div class="brand">
    <span class="brand-dot"></span>
    <p class="brand-name">Peak Motion<br>Athletic Care</p>
  </div>
  <p class="brand-address">Linden Gardens, Adelaide,<br>South Australia 5071</p>

  <ul class="practice-list">
    <li>KineCore<br>418 Tolley Rd Kestrel Vale<br>84619032<br>Monday Wednesday Friday</li>
    <li>Harrow Lane Sports Clinic<br>153 Denholm Rd, Adelaide<br>81764290<br>Tuesday</li>
    <li>Riverbend Falcons Sports Medicine Clinic<br>Norvale Park<br>8291 6475<br>Thursday</li>
  </ul>

  <p class="website">www.peakmotionathleticcare.com</p>

  <h1 class="doctor-name">DR. PAUL DENTON</h1>

  <section class="info-panel">
    <p class="lead">• Sports medicine doctor specialising in the diagnosis and management of sport and exercise injuries</p>

    <h2 class="section-title">Background:</h2>
    <ul>
      <li>• Masters in Sports Medicine (MSportsMed)</li>
      <li>• Diplomas in Obstetrics/Gynaecology (DRANZCOG) and also Paediatrics (DCH)</li>
      <li>• Certificate in advanced clinical hypnosis</li>
      <li>• Works with Clara Hutchings ex Australian Athlete, a Performance Strategist (NRC listed resource person) and registered Psychologist for best mental preparation for individuals teams and coach development</li>
    </ul>

    <h2 class="section-title offers">Offers...</h2>
    <ul>
      <li>• Accurate diagnosis and management plan with their regular physio to return the player / athlete to the field / court /gym as soon as safely possible</li>
      <li>• Hypnosis for sports performance eg anxiety control, confidence and mental rehearsal for individuals and teams</li>
      <li>• Recommendation for one point of contact for coaches and clubs for rehabilitation and return to sport advice.</li>
      <li>• Organizing rapid access to MRI, ultrasound and specialist appointments if needed.</li>
    </ul>
  </section>
</main>
</body>
</html>
```